LOGO and PACKAGING Memory Foam Slipper

Need a logo and packages (mens and women versions) designed for a new line of memory foam Moccasins. "Marcus Whitfield Designer Collection" Should communicate premium quality features. Will provide dielines, for the box.

```html
<!DOCTYPE html>
<html lang="en">
<head>
<meta charset="utf-8">
<title>Marcus Whitfield Designer Collection – Slipper Box Dieline</title>
<link href="https://fonts.googleapis.com/css2?family=Playfair+Display:wght@400&family=Open+Sans:wght@400&display=swap" rel="stylesheet">
<style>
  :root{
    --bg:#ffffff;
    --board:#dfc9a5;
    --flap:#b9a288;
    --mark:#bea789;
    --ribbon:#cc9095;
    --ribbon-soft:#d9aaae;
    --ink:#5f5f62;
    --cut:#d9d2c8;
    --fold:#cbb48f;
  }
  html,body{margin:0;padding:0;width:1070px;height:1200px;overflow:hidden;background:var(--bg);}
  .dieline{display:block;width:1070px;height:1200px;}
  .panel{fill:var(--board);}
  .flap{fill:var(--flap);}
  .tuck{fill:#fff;stroke:var(--cut);stroke-width:1;}
  .window{fill:#fff;}
  .fold-line{stroke:var(--fold);stroke-width:0.8;fill:none;}
  .perforation{stroke:#ddd;stroke-width:1;stroke-dasharray:4 3;}
  .ribbon{fill:var(--ribbon);}
  .brand-name{font-family:"Playfair Display",serif;fill:var(--ink);}
  .brand-line{font-family:"Open Sans",sans-serif;fill:var(--ink);letter-spacing:0.3px;}
  .brand-watermark{font-family:"Playfair Display",serif;fill:var(--mark);}
  .brand-square{fill:var(--ink);}
</style>
</head>
<body>
<svg class="dieline" viewBox="0 0 892 1000" xmlns="http://www.w3.org/2000/svg" role="img" aria-label="Flat box dieline for Marcus Whitfield Designer Collection slippers">
  <defs>
    <linearGradient id="band-fill" x1="0" y1="0" x2="1" y2="0">
      <stop offset="0" stop-color="var(--ribbon)"/>
      <stop offset="0.5" stop-color="var(--ribbon-soft)"/>
      <stop offset="1" stop-color="var(--ribbon)"/>
    </linearGradient>
  </defs>

  <!-- tuck tabs -->
  <path class="tuck" d="M232 115 H210 Q205 115 205 120 V170 Q205 175 210 175 H232 Z"/>
  <path class="tuck" d="M660 115 H683 Q688 115 688 120 V170 Q688 175 683 175 H660 Z"/>
  <rect class="tuck" x="28" y="597" width="12" height="66"/>
  <rect class="tuck" x="852" y="597" width="12" height="66"/>
  <path class="tuck" d="M232 960 V990 Q232 1000 242 1000 H650 Q660 1000 660 990 V960 Z"/>

  <!-- dust flaps -->
  <polygon class="flap" points="232,300 232,476 170,476 170,385 205,345 232,345"/>
  <polygon class="flap" points="660,300 660,476 722,476 722,385 687,345 660,345"/>
  <polygon class="flap" points="232,785 232,960 205,960 205,925 170,885 170,785"/>
  <polygon class="flap" points="660,785 660,960 687,960 687,925 722,885 722,785"/>

  <!-- side glue strips -->
  <path class="flap" d="M38 485 H10 Q0 485 0 495 V765 Q0 775 10 775 H38 Z"/>
  <path class="flap" d="M853 485 H882 Q892 485 892 495 V765 Q892 775 882 775 H853 Z"/>

  <!-- main panels -->
  <rect class="panel" x="232" y="0" width="428" height="968"/>
  <rect class="panel" x="38" y="485" width="194" height="290"/>
  <rect class="panel" x="660" y="485" width="193" height="290"/>

  <!-- window -->
  <rect class="window" x="358" y="293" width="175" height="318"/>
  <line class="perforation" x1="358" y1="418" x2="533" y2="418"/>

  <!-- fold lines -->
  <line class="fold-line" x1="232" y1="293" x2="358" y2="293"/>
  <line class="fold-line" x1="533" y1="293" x2="660" y2="293"/>
  <line class="fold-line" x1="232" y1="485" x2="358" y2="485"/>
  <line class="fold-line" x1="533" y1="485" x2="660" y2="485"/>
  <line class="fold-line" x1="232" y1="775" x2="660" y2="775"/>
  <line class="fold-line" x1="232" y1="485" x2="232" y2="775"/>
  <line class="fold-line" x1="660" y1="485" x2="660" y2="775"/>

  <!-- vertical decorative band (pattern area, flat fill) -->
  <g role="img" aria-label="Vertical pink pinstripe decorative band">
    <rect x="550" y="0" width="90" height="968" fill="url(#band-fill)"/>
  </g>

  <!-- horizontal ribbons -->
  <rect class="ribbon" x="38" y="515" width="320" height="25"/>
  <text class="brand-line" x="64" y="533" font-size="11">DESIGNER COLLECTION</text>
  <rect class="ribbon" x="533" y="736" width="320" height="25"/>
  <text class="brand-line" x="818" y="748" font-size="11" text-anchor="start" transform="rotate(180 772 748)" dy="4">DESIGNER COLLECTION</text>

  <!-- lid panel -->
  <text class="brand-line" x="446" y="24" font-size="11" text-anchor="middle" transform="rotate(180 446 20)">DESIGNER COLLECTION</text>
  <text class="brand-watermark" x="391" y="150" font-size="34" text-anchor="middle" transform="rotate(180 391 150)">Marcus Whitfield</text>

  <!-- end flap with vertical name -->
  <g transform="translate(295 388) rotate(-90)">
    <text class="brand-name" x="0" y="0" font-size="19" text-anchor="middle">Marcus Whitfield</text>
    <text class="brand-line" x="0" y="24" font-size="10" text-anchor="middle">DESIGNER COLLECTION</text>
  </g>

  <!-- side panels -->
  <text class="brand-watermark" x="135" y="640" font-size="21" text-anchor="middle" transform="rotate(180 135 633)">Marcus Whitfield</text>
  <text class="brand-watermark" x="757" y="640" font-size="21" text-anchor="middle" transform="rotate(180 757 633)">Marcus Whitfield</text>

  <!-- front panel -->
  <g class="brand-lockup">
    <rect class="brand-square" x="252" y="624" width="14" height="14"/>
    <text class="brand-name" x="252" y="668" font-size="24">Marcus</text>
    <text class="brand-name" x="252" y="698" font-size="24">Whitfield</text>
  </g>
  <text class="brand-name" x="378" y="679" font-size="21">Marcus Whitfield</text>
  <text class="brand-line" x="395" y="699" font-size="11">DESIGNER COLLECTION</text>
</svg>
</body>
</html>
```